Birchline Septic Solutions

Would like to see some single sided ones but would also like to see some double sided with one sided only being the logo. Owners name is Tom Waldrick. Phone number is 555-214-8830
Services are pumping, inspections, installs, and repairs

Contact Information for Business Card

555-241-8830 Tom Waldrick Alderbrook, OH

```html
<!DOCTYPE html>
<html lang="en">
<head>
<meta charset="utf-8">
<title>Birchline Septic Solutions – Business Card</title>
<link rel="stylesheet" href="https://fonts.googleapis.com/css2?family=Arimo:wght@400;700&display=swap">
<style>
  :root {
    --card: #2a2a2a;
    --card-soft: #3b3b3b;
    --teal: #2bbab2;
    --white: #ffffff;
    --muted: #d9d9d9;
    --page: #e8e8e8;
  }
  * { box-sizing: border-box; margin: 0; padding: 0; }
  html, body { width: 1200px; height: 802px; overflow: hidden; }
  body {
    background: var(--page);
    font-family: "Arimo", Arial, sans-serif;
    position: relative;
  }
  .card {
    position: absolute;
    top: 246px;
    width: 540px;
    height: 309px;
    background: var(--card);
    border-bottom: 4px solid var(--teal);
    overflow: hidden;
  }
  .card--front { left: 40px; }
  .card--back { left: 620px; }

  .corner-tab {
    position: absolute;
    top: 0; right: 0;
    width: 18px; height: 40px;
    background: var(--teal);
  }
  .owner {
    position: absolute;
    top: 28px; right: 40px;
    text-align: right;
  }
  .owner__name {
    color: var(--teal);
    font-size: 25px;
    font-weight: 400;
    letter-spacing: 0.5px;
    text-transform: uppercase;
  }
  .owner__title {
    color: var(--white);
    font-size: 16px;
    margin-top: 2px;
  }
  .scenery {
    position: absolute;
    right: 0; bottom: 0;
    width: 320px; height: 240px;
    background: linear-gradient(160deg, transparent 20%, var(--card-soft) 60%, #353535 100%);
    opacity: 0.8;
  }
  .wordmark {
    color: var(--white);
    font-weight: 700;
    line-height: 1;
    display: flex;
    align-items: center;
    gap: 12px;
  }
  .wordmark__mark {
    width: 14px; height: 14px;
    background: var(--teal);
    flex: none;
  }
  .wordmark__name { font-size: 34px; letter-spacing: 1px; }
  .wordmark__sub {
    display: block;
    font-size: 13px;
    letter-spacing: 4px;
    margin-top: 8px;
  }
  .card--front .wordmark {
    position: absolute;
    left: 40px; top: 118px;
  }
  .contact {
    position: absolute;
    left: 40px; bottom: 34px;
    color: var(--muted);
    font-size: 15px;
  }
  .contact__phone {
    display: flex;
    align-items: center;
    gap: 7px;
    margin-top: 8px;
    color: var(--white);
    font-weight: 700;
    font-size: 17px;
  }
  .card--back .wordmark {
    position: absolute;
    left: 50%; top: 50%;
    transform: translate(-50%, -50%);
  }
  .card--back .wordmark__name { font-size: 44px; }
  .card--back .wordmark__sub { font-size: 16px; letter-spacing: 6px; }
</style>
</head>
<body>
  <section class="card card--front" aria-label="Business card front">
    <div class="corner-tab"></div>
    <div class="scenery" role="img" aria-label="Faint mountain and pine tree backdrop"></div>
    <div class="owner">
      <p class="owner__name">Tom Waldrick</p>
      <p class="owner__title">Owners</p>
    </div>
    <div class="wordmark">
      <span class="wordmark__mark"></span>
      <p class="wordmark__name">BIRCHLINE<span class="wordmark__sub">SEPTIC SOLUTIONS</span></p>
    </div>
    <div class="contact">
      <p class="contact__city">Alderbrook, OH</p>
      <p class="contact__phone">
        <svg width="14" height="14" viewBox="0 0 24 24" aria-hidden="true">
          <path fill="#2bbab2" d="M6.6 10.8a15.1 15.1 0 0 0 6.6 6.6l2.2-2.2a1 1 0 0 1 1-.25 11.4 11.4 0 0 0 3.6.57 1 1 0 0 1 1 1V20a1 1 0 0 1-1 1A17 17 0 0 1 3 4a1 1 0 0 1 1-1h3.5a1 1 0 0 1 1 1c0 1.25.2 2.45.57 3.57a1 1 0 0 1-.25 1z"/>
        </svg>
        555-214-8830
      </p>
    </div>
  </section>

  <section class="card card--back" aria-label="Business card back">
    <div class="wordmark">
      <span class="wordmark__mark"></span>
      <p class="wordmark__name">BIRCHLINE<span class="wordmark__sub">SEPTIC SOLUTIONS</span></p>
    </div>
  </section>
</body>
</html>
```